Quick & Dirty Poster Design Project - A2 Posters

I run a business called Terra Lumen. We sell high end outdoor flooring and walling (natural stone products) to architects and designers.

We work mainly with high end landscape designers on garden design and outdoor architecture.

Our sales teams provide advice and expertise and sell architectural design products to architects and designers.

I wanted to design some fun A2 posters to put in the sales offices just to create a bit of energy and momentum for staff. These are for internal use only.

The 4 copy lines are:

1.Beware of people who don't get their hands dirty

2. If you don't take a chance you won't have one

3. Having trouble getting started? Quit talking and start doing

4. Remember the questions you ask are more important than anything you could ever say

Just one copy line for each poster

(Pls note due to the limited budget and timings, I'm expecting interesting typeset posters not "designed" artworks). Thanks

Target Market(s)

sales team

Industry/Entity Type

Landscape

Requirements
Must have
• Our logo (Terra Lumen) - I have provided a few versions of the logo
Nice to have
• Some design element alongside the typeface / copy

```html
<!DOCTYPE html>
<html lang="en">
<head>
<meta charset="utf-8">
<title>Terra Lumen — Remember the Questions</title>
<link rel="stylesheet" href="https://fonts.googleapis.com/css2?family=Anton&display=swap">
<style>
  :root {
    --page: #ffffff;
    --poster: #42037a;
    --ink: #ffffff;
    --line: #000000;
    --figure-tone: #6a3a99;
  }
  html, body {
    margin: 0;
    padding: 0;
    width: 1200px;
    height: 900px;
    overflow: hidden;
    background: var(--page);
  }
  .canvas {
    position: relative;
    width: 1200px;
    height: 900px;
  }
  .poster {
    position: absolute;
    left: 297px;
    top: 18px;
    width: 580px;
    height: 830px;
    background: var(--poster);
  }
  .poster svg {
    display: block;
    width: 580px;
    height: 830px;
  }
  .headline text {
    font-family: "Anton", "Oswald", sans-serif;
    fill: var(--ink);
    text-transform: uppercase;
  }
  .ground-line {
    stroke: var(--line);
    stroke-width: 3;
  }
  .figure-placeholder {
    fill: var(--figure-tone);
  }
  .brand-mark {
    fill: var(--ink);
  }
  .brand-name {
    font-family: "Anton", "Oswald", sans-serif;
    fill: var(--ink);
    font-size: 16px;
  }
</style>
</head>
<body>
<main class="canvas">
  <section class="poster">
    <svg viewBox="0 0 580 830" xmlns="http://www.w3.org/2000/svg">
      <g class="headline">
        <text x="128" y="122" font-size="72" textLength="337" lengthAdjust="spacingAndGlyphs">Remember</text>
        <text x="128" y="174" font-size="53" textLength="337" lengthAdjust="spacingAndGlyphs">The Questions</text>
        <text x="128" y="264" font-size="97" textLength="337" lengthAdjust="spacingAndGlyphs">You Ask</text>
        <text x="128" y="300" font-size="34" textLength="337" lengthAdjust="spacingAndGlyphs">Are More Important</text>
        <text x="128" y="328" font-size="25" textLength="337" lengthAdjust="spacingAndGlyphs">Than Anything You Could Ever</text>
        <text x="128" y="510" font-size="204" textLength="337" lengthAdjust="spacingAndGlyphs">Say</text>
      </g>

      <rect class="figure-placeholder" x="205" y="558" width="160" height="166" rx="6"
            role="img" aria-label="Simple line-drawn cartoon character scratching its head, with question marks floating around it"/>

      <line class="ground-line" x1="0" y1="726" x2="580" y2="726"/>

      <g class="brand">
        <circle class="brand-mark" cx="466" cy="778" r="7"/>
        <text class="brand-name" x="480" y="784">Terra Lumen</text>
      </g>
    </svg>
  </section>
</main>
</body>
</html>
```